TALL WAVE

I am in this industry for last 15 years we have done lots of commercial site like we work with ORBEL costruction, loam properties, DRV, quill construction.
We do all domestic and commercial wall and floor tiling, swimming pools, spas, paving, marbles blue stones and muchmore.

Specializing in the wall and floor Tiling, Waterproofing and floor preparations

Industry/Entity Type

Industry

Number of Pages Required

1 page

Font styles to use
Serif
Decorative

Colors

Designer to choose colors to be used in the design.

Requirements
Must have
• domestic and commercial indoor tiling, bathroom tiling and paving pictures
Nice to have
• beautiful bathroom pictures with tile

```html
<!DOCTYPE html>
<html lang="en">
<head>
<meta charset="utf-8">
<title>TALL WAVE — Wall &amp; Floor Tiling</title>
<link href="https://fonts.googleapis.com/css2?family=Lato:ital,wght@0,400;0,700;0,900;1,700&family=Open+Sans+Condensed:wght@700&display=swap" rel="stylesheet">
<style>
:root{
  --blue:#1f8fd8;
  --blue-dark:#1a78b8;
  --ink:#1c1c1c;
  --text:#555;
  --muted:#8a8a8a;
  --white:#fff;
  --dark:#1b1d20;
  --footer:#262626;
  --line:#d6d6d6;
}
*{margin:0;padding:0;box-sizing:border-box}
html,body{width:1200px;height:3422px;overflow:hidden}
body{position:relative;font-family:"Lato",Arial,sans-serif;color:var(--text);background:var(--white)}
.abs{position:absolute}

/* header */
.site-header{position:absolute;left:0;top:0;width:1200px;height:135px;background:var(--white);display:flex;align-items:center;justify-content:center;gap:34px;padding-top:4px}
.nav{display:flex;gap:30px;font-family:"Open Sans Condensed","Arial Narrow",sans-serif;font-weight:700;font-size:15px;letter-spacing:1px;color:var(--ink);white-space:nowrap}
.brand{display:flex;align-items:center;gap:12px;white-space:nowrap}
.brand-mark{width:38px;height:38px;background:var(--blue)}
.brand-name{font-family:"Lato",sans-serif;font-weight:900;font-size:29px;color:var(--ink);letter-spacing:.5px}

/* hero */
.hero{position:absolute;left:0;top:135px;width:1200px;height:634px;background:radial-gradient(ellipse at 55% 70%,#5b6670 0%,#2b3238 45%,#12161a 100%)}
.hero-title{position:absolute;left:0;width:1200px;top:168px;text-align:center;color:var(--white);font-weight:900;font-size:54px;line-height:57px;letter-spacing:2px}
.accent-bar{position:absolute;height:5px;background:var(--blue)}
.hero-text{position:absolute;left:365px;width:470px;top:318px;text-align:center;color:var(--white);font-weight:700;font-size:14px;line-height:26px}
.btn-light{position:absolute;left:515px;top:400px;width:169px;height:45px;background:var(--white);color:var(--ink);font-weight:900;font-size:14px;letter-spacing:1px;display:flex;align-items:center;justify-content:center}

/* about */
.about-title{left:125px;top:840px;font-weight:900;font-size:32px;color:var(--ink);letter-spacing:1px}
.about-sub{left:119px;top:922px;font-weight:700;font-size:20px;color:var(--blue);letter-spacing:.5px}
.about-text{left:119px;top:970px;width:500px;font-size:13.5px;line-height:20.5px;color:var(--text)}
.btn-blue{position:absolute;background:var(--blue);color:var(--white);font-weight:900;font-size:13px;letter-spacing:1px;display:flex;align-items:center;justify-content:center}
.about-sketch{left:684px;top:867px;width:434px;height:376px;background:linear-gradient(135deg,#fafafa,#e9e9e9)}

/* services */
.services{position:absolute;left:0;top:1289px;width:1200px;height:554px;background:radial-gradient(ellipse at 60% 40%,#3a3d40 0%,#17191b 80%)}
.section-title{position:absolute;left:0;width:1200px;text-align:center;font-weight:900;font-size:32px;letter-spacing:1.5px}
.section-sub{position:absolute;left:0;width:1200px;text-align:center;font-size:12.5px;line-height:22px}
.card{position:absolute;width:326px;background:var(--white)}
.card-photo{width:326px;height:192px}
.card-title{margin-top:20px;text-align:center;font-weight:900;font-size:19px;line-height:26px;color:var(--ink);letter-spacing:.5px}
.card-text{margin:14px auto 0;width:250px;text-align:center;font-size:13px;line-height:20px;color:var(--muted)}
.card.is-active{background:var(--blue)}
.card.is-active .card-title,.card.is-active .card-text{color:var(--white)}

/* projects */
.project{position:absolute;width:326px}
.project-photo{width:326px;height:226px}
.project-title{margin-top:24px;text-align:center;font-weight:900;font-size:19px;color:var(--ink);letter-spacing:.5px}
.project-text{margin:10px auto 0;width:290px;text-align:center;font-size:13px;line-height:20px;color:var(--muted)}
.project-rule{position:absolute;left:0;top:353px;width:326px;height:3px;background:var(--line)}
.project.is-active .project-rule{background:var(--blue)}

/* testimonials + contact */
.feedback{position:absolute;left:0;top:2480px;width:1200px;height:444px;background:radial-gradient(ellipse at 30% 70%,#2f4856 0%,#16202a 55%,#0e1216 100%)}
.testimonial-title{left:100px;top:2564px;font-weight:900;font-size:32px;color:var(--white);letter-spacing:1.5px}
.testimonial-sub{left:103px;top:2608px;font-size:13px;color:#cfd6db}
.quote-box{left:100px;top:2646px;width:445px;height:182px;background:rgba(70,74,78,.75);padding:40px 30px 0 30px;color:var(--white);font-size:13px;line-height:20.5px}
.quote-author{position:absolute;right:32px;bottom:28px;color:var(--blue);font-weight:700;font-size:13px}
.contact-panel{position:absolute;left:655px;top:2480px;width:447px;height:444px;background:rgba(28,30,33,.92);overflow:hidden}
.contact-title{position:absolute;left:26px;top:24px;font-weight:900;font-size:24px;color:var(--white);letter-spacing:.5px}
.field{position:absolute;left:98px;width:273px;background:var(--white);font-size:11.5px;color:#555;padding:10px 12px}

/* call bar */
.call-bar{position:absolute;left:0;top:2924px;width:1200px;height:110px;background:var(--blue);display:flex;align-items:center;justify-content:center;color:var(--white);font-weight:700;font-size:22px;letter-spacing:1px}
.call-bar em{font-style:italic;margin-left:8px}
.call-bar .call-number{font-style:italic;font-weight:700;font-size:30px;margin-left:12px}

/* footer */
.site-footer{position:absolute;left:0;top:3034px;width:1200px;height:388px;background:var(--footer);color:var(--white)}
.footer-nav{position:absolute;left:0;width:1200px;top:52px;display:flex;justify-content:center;font-family:"Open Sans Condensed","Arial Narrow",sans-serif;font-weight:700;font-size:16px;letter-spacing:1px}
.footer-nav span{padding:0 24px;border-left:2px solid var(--white);line-height:14px}
.footer-nav span:first-child{border-left:none}
.contact-list{position:absolute;left:0;width:1200px;top:104px;text-align:center;font-size:17px;line-height:32px;letter-spacing:1px}
.contact-list b{color:var(--blue);font-weight:900;margin-right:8px}
.socials{position:absolute;left:0;width:1200px;top:256px;display:flex;justify-content:center;gap:22px}
.social-dot{width:24px;height:24px;border-radius:50%;background:var(--white)}
.footer-rule{position:absolute;left:115px;top:315px;width:970px;height:1px;background:#3d3d3d}
.copyright{position:absolute;left:0;width:1200px;top:341px;text-align:center;font-size:16px;letter-spacing:2px;color:#d9d9d9}
</style>
</head>
<body>

<header class="site-header">
  <nav class="nav nav-left"><span>HOME</span><span>SERVICES</span><span>PORTFOLIO</span></nav>
  <div class="brand"><div class="brand-mark"></div><div class="brand-name">TALL WAVE</div></div>
  <nav class="nav nav-right"><span>PROJECTS</span><span>BLOG</span><span>CONTACT US</span></nav>
</header>

<section class="hero" role="img" aria-label="Dark photo of a modern tiled bathroom with a freestanding bath">
  <h1 class="hero-title">LOREM IPSUM<br>DOLOR SIT</h1>
  <div class="accent-bar" style="left:566px;top:296px;width:68px"></div>
  <p class="hero-text">Cras rutrum varius pretium. Pellentesque elit est, tempus at sollicitudin sed, placerat in magna.</p>
  <div class="btn-light">READ MORE</div>
</section>

<section class="about">
  <h2 class="abs about-title">About Us</h2>
  <div class="accent-bar" style="left:125px;top:886px;width:82px;height:3px;background:var(--ink)"></div>
  <h3 class="abs about-sub">Welcome to TALL WAVE</h3>
  <p class="abs about-text">Lorem ipsum dolor sit amet, consectetur adipiscing elit. In lobortis in mi ac porta. Cras rutrum varius pretium. Pellentesque elit est, tempus at sollicitudin sed, placerat in magna. Lorem ipsum dolor sit amet, consectetur adipiscing elit. Nunc pretium placerat semper. Nam scelerisque dolor sed libero accumsan porta. Cras id mi at est egestas sodales. Donec a diam cursus, posuere eros ut, tincidunt lacus. Phasellus eu dignissim ipsum.</p>
  <div class="btn-blue" style="left:119px;top:1157px;width:171px;height:45px">READ MORE</div>
  <div class="abs about-sketch" role="img" aria-label="Line sketch of a bathroom interior with bath, window and tiled floor"></div>
</section>

<section class="services" role="img" aria-label="Dark tiled background photo">
  <h2 class="section-title" style="top:40px;color:var(--white)">Services</h2>
  <p class="section-sub" style="top:94px;color:#cfcfcf">Phasellus sit amet blandit dolor, vel fringilla tellus.</p>
  <article class="card" style="left:94px;top:155px;height:331px">
    <div class="card-photo" role="img" aria-label="Hands laying wall tiles" style="background:linear-gradient(135deg,#8a5a36,#c9a27a 55%,#5c3b24)"></div>
    <h3 class="card-title">Wall Tiling</h3>
    <p class="card-text">Mauris pharetra ipsum congue mollis tincidunt. Fusce vel dignissim sapie.</p>
  </article>
  <article class="card is-active" style="left:438px;top:155px;height:331px">
    <div class="card-photo" role="img" aria-label="Tiler spreading adhesive on a floor" style="background:linear-gradient(135deg,#d9d4cc,#a9a198 60%,#6e6660)"></div>
    <h3 class="card-title">Floor Tiling</h3>
    <p class="card-text">Mauris pharetra ipsum congue mollis tincidunt. Fusce vel dignissim sapie.</p>
  </article>
  <article class="card" style="left:780px;top:155px;height:331px">
    <div class="card-photo" role="img" aria-label="Worker applying waterproofing to a floor" style="background:linear-gradient(135deg,#2b3f6e,#9da3a8 55%,#d6d6d2)"></div>
    <h3 class="card-title">Waterproofing and<br>floor preparations</h3>
    <p class="card-text">Mauris pharetra ipsum congue mollis tincidunt. Fusce vel dignissim sapie.</p>
  </article>
</section>

<section class="projects">
  <h2 class="section-title" style="top:1912px;color:var(--ink)">Latest Projects</h2>
  <p class="section-sub" style="top:1982px;color:var(--muted)">Proin leo velit, tempus non nibh quis, fermentum facilisis<br>lorem. Praesent eget leo non orci egestas sodales quis vitae</p>
  <article class="project is-active" style="left:94px;top:2069px">
    <div class="project-photo" role="img" aria-label="Outdoor paved terrace beside a building" style="background:linear-gradient(160deg,#e4e4e2,#a7a39d 60%,#6b6863)"></div>
    <h3 class="project-title">Lorem ipsum dolor</h3>
    <p class="project-text">Cras id mi at est egestas sodales. Donec a diam cursus, posuere eros ut.</p>
    <div class="project-rule"></div>
  </article>
  <article class="project" style="left:438px;top:2069px">
    <div class="project-photo" role="img" aria-label="Indoor swimming pool with blue tiles" style="background:linear-gradient(180deg,#5d6b72,#2a4a5c 55%,#1d5d7e)"></div>
    <h3 class="project-title">Lorem ipsum dolor</h3>
    <p class="project-text">Cras id mi at est egestas sodales. Donec a diam cursus, posuere eros ut.</p>
    <div class="project-rule"></div>
  </article>
  <article class="project" style="left:780px;top:2069px">
    <div class="project-photo" role="img" aria-label="Bathroom with beige stone tiles and bath" style="background:linear-gradient(135deg,#e8d6bd,#c4a57e 55%,#8d6c4c)"></div>
    <h3 class="project-title">Lorem ipsum dolor</h3>
    <p class="project-text">Cras id mi at est egestas sodales. Donec a diam cursus, posuere eros ut.</p>
    <div class="project-rule"></div>
  </article>
</section>

<section class="feedback" role="img" aria-label="Dusk photo of a tiled swimming pool">
</section>
<h2 class="abs testimonial-title">Testimonials</h2>
<p class="abs testimonial-sub">Phasellus sit amet blandit tellus.</p>
<blockquote class="abs quote-box">Lorem ipsum dolor sit amet, consectetur adipiscing elit. In lobortis in mi ac porta. Cras rutrum varius pretium. Pellentesque elit est, tempus at sollicitudin sed, placerat in magna.<span class="quote-author">Ned Corrin</span></blockquote>

<aside class="contact-panel">
  <svg class="abs" style="left:0;top:0" width="447" height="104" viewBox="0 0 447 104">
    <polygon points="0,0 447,0 447,32 0,104" fill="#1f8fd8"/>
  </svg>
  <h2 class="contact-title">Email Us</h2>
  <div class="field" style="top:127px;height:37px">Name...</div>
  <div class="field" style="top:182px;height:36px">Email...</div>
  <div class="field" style="top:237px;height:89px">Message...</div>
  <div class="btn-blue" style="left:157px;top:353px;width:171px;height:43px">SUBMIT</div>
</aside>

<div class="call-bar">Get a Professional Services, <em>Call us Now.</em><span class="call-number">555 010 264</span></div>

<footer class="site-footer">
  <nav class="footer-nav"><span>HOME</span><span>SERVICES</span><span>PORTFOLIO</span><span>PROJECTS</span><span>BLOG</span><span>CONTACT US</span></nav>
  <div class="contact-list">
    <div><b>ADDRESS</b>48 Harbor Row, Fairview</div>
    <div><b>EMAIL</b>HELLO@TALLWAVE.TEST</div>
    <div><b>PHONE</b>+1 555 010 482</div>
    <div><b>FAX</b>+1 555 010 733</div>
  </div>
  <div class="socials"><span class="social-dot"></span><span class="social-dot"></span><span class="social-dot"></span><span class="social-dot"></span></div>
  <div class="footer-rule"></div>
  <p class="copyright">© 2017 &nbsp;TALL WAVE All rights reserved.</p>
</footer>

</body>
</html>
```